TV Antenna Installation business needs a unique flyer

We need a simple but effective flyer design for our TV Aerial installation company based in Newcastle, NSW, Australia called Clearpeak TV & Aerial Svcs.
We are trying to target areas where there has been a new transmitter installed and most houses just require their aerial redirecting and tv's retuning.

Industry/Entity Type

Business

Requirements
Must have
• We would like the idea of a headline phrase such as " Poor TV reception……..now a thing from the past" or something similar & catchy.
Also "Did you know a new transmitter has been recently installed in your area, we can therefore now GUARANTEE 100% PERFECT PICTURE
Charges from only $95.
- Free 5 year warranty
- Free signal testing
- Free Onsite Quote
Phone 0452 736 205
Nice to have
• Other services include:

- New Installs
- Extra Points & repairs
- TV wall mounting/Home Cinema
- Pull down tall masts

Modern tv picture, see example uploaded

```html
<!DOCTYPE html>
<html lang="en">
<head>
<meta charset="utf-8">
<title>Clearpeak TV &amp; Aerial Svcs – Flyer</title>
<link href="https://fonts.googleapis.com/css2?family=Bree+Serif&family=Open+Sans:ital,wght@0,400;0,600;0,700;1,400&display=swap" rel="stylesheet">
<style>
  :root{
    --orange:#f05a28;
    --blue:#1a70b8;
    --grey:#6d6e70;
    --text-grey:#5f6062;
    --white:#ffffff;
    --tv-gold:#b49a52;
    --tv-dark:#3a3a3a;
  }
  *{margin:0;padding:0;box-sizing:border-box}
  html,body{width:897px;height:1200px;overflow:hidden;background:var(--white)}
  .flyer{position:relative;width:897px;height:1200px;background:var(--white);font-family:"Open Sans",Arial,sans-serif;overflow:hidden}
  .wave{position:absolute;left:0;width:897px}
  .wave--top{top:0;height:240px}
  .wave--bottom{bottom:0;height:200px}
  .brand{position:absolute;left:30px;top:28px;display:flex;align-items:center;gap:14px;color:var(--white);font-family:"Bree Serif",Georgia,serif;font-size:60px;line-height:1}
  .brand__dot{width:22px;height:22px;border-radius:50%;background:var(--white)}
  .headline{position:absolute;left:43px;top:245px;color:var(--orange);font-family:"Bree Serif",Georgia,serif;font-weight:400;line-height:1.08}
  .headline__main{display:block;font-size:78px}
  .headline__sub{display:block;font-size:62px}
  .tagline{position:absolute;left:43px;top:462px;color:var(--grey);font-family:"Bree Serif",Georgia,serif;font-size:47px;line-height:1.3;font-weight:400}
  .tv-image{position:absolute;left:392px;top:140px;width:478px;height:480px;border-radius:40px;background:radial-gradient(ellipse 60% 55% at 50% 55%, #9a9a9a 0%, var(--tv-dark) 55%, var(--tv-gold) 100%)}
  .intro{position:absolute;left:40px;top:676px;width:372px;color:var(--text-grey);font-size:21px;line-height:37px;text-align:justify;letter-spacing:.2px;hyphens:manual}
  .intro strong{font-weight:700}
  .intro .accent{color:var(--blue);font-weight:700}
  .intro .caps{font-weight:700;letter-spacing:2.5px}
  .offer{position:absolute;left:449px;top:667px;width:422px;height:208px;background:var(--blue);outline:2px solid var(--blue);outline-offset:3px;border:2px solid var(--white);color:var(--white);text-align:center;padding-top:26px}
  .offer__price{font-size:30px;font-weight:600;line-height:40px;margin-bottom:4px}
  .offer__perk{font-size:27px;font-style:italic;line-height:43px}
  .services-tag{position:absolute;left:422px;top:912px;width:445px;height:54px;color:var(--white);font-size:30px;font-weight:600;display:flex;align-items:center;justify-content:flex-end;padding-right:14px}
  .services-tag svg{position:absolute;inset:0;z-index:0}
  .services-tag span{position:relative;z-index:1}
  .services{position:absolute;left:26px;top:916px;list-style:none;color:var(--grey);font-size:27px;font-style:italic;line-height:42px;z-index:2}
  .services li{display:flex;align-items:center;gap:14px}
  .services svg{width:26px;height:26px;flex:none}
  .phone{position:absolute;right:30px;bottom:24px;display:flex;align-items:center;gap:10px;color:var(--white);font-size:52px;font-weight:700;letter-spacing:1px}
  .phone svg{width:50px;height:50px}
</style>
</head>
<body>
<div class="flyer">
  <svg class="wave wave--top" viewBox="0 0 897 240" preserveAspectRatio="none" aria-hidden="true">
    <path d="M0 0H897V112C760 100 600 125 430 160C250 195 110 195 0 180Z" fill="var(--orange)"/>
    <path d="M300 200C520 180 700 122 897 108V130C700 136 540 182 300 200Z" fill="var(--blue)"/>
  </svg>

  <div class="brand"><span>clearpeak</span><span class="brand__dot"></span></div>

  <h1 class="headline"><span class="headline__main">Poor TV</span><span class="headline__sub">reception</span></h1>
  <h2 class="tagline">NOW a thing<br>from the past</h2>

  <div class="tv-image" role="img" aria-label="Photo of a retro television with antennas showing a static-filled screen"></div>

  <p class="intro">Did you know a new&shy;trans&shy;mitter has been recently installed in your area, we can therefore now <strong>GUARANTEE</strong> <span class="accent">100%</span> <span class="caps">PERFECT PICTURE</span></p>

  <div class="offer">
    <p class="offer__price">Charges from only $95</p>
    <p class="offer__perk">+ Free 5 years warranty</p>
    <p class="offer__perk">+ Free signal testing</p>
    <p class="offer__perk">+ Free Onsite Quote</p>
  </div>

  <div class="services-tag">
    <svg viewBox="0 0 445 54" preserveAspectRatio="none" aria-hidden="true"><path d="M0 27L26 0H445V54H26Z" fill="var(--orange)"/></svg>
    <span>Other services include</span>
  </div>

  <svg class="wave wave--bottom" viewBox="0 0 897 200" preserveAspectRatio="none" aria-hidden="true">
    <path d="M0 132C200 150 420 112 620 62C720 42 800 38 897 40V200H0Z" fill="var(--orange)"/>
    <path d="M0 112C200 138 420 100 640 46C430 112 200 150 0 136Z" fill="var(--blue)"/>
  </svg>

  <ul class="services">
    <li><svg viewBox="0 0 26 26" aria-hidden="true"><rect x="2" y="7" width="17" height="17" fill="none" stroke="var(--grey)" stroke-width="2"/><path d="M6 14l5 5L23 4" fill="none" stroke="var(--orange)" stroke-width="3.5"/></svg>New Installs</li>
    <li><svg viewBox="0 0 26 26" aria-hidden="true"><rect x="2" y="7" width="17" height="17" fill="none" stroke="var(--grey)" stroke-width="2"/><path d="M6 14l5 5L23 4" fill="none" stroke="var(--orange)" stroke-width="3.5"/></svg>Extra Points &amp; repairs</li>
    <li><svg viewBox="0 0 26 26" aria-hidden="true"><rect x="2" y="7" width="17" height="17" fill="none" stroke="var(--grey)" stroke-width="2"/><path d="M6 14l5 5L23 4" fill="none" stroke="var(--orange)" stroke-width="3.5"/></svg>TV wall mounting/Home Cinema</li>
    <li><svg viewBox="0 0 26 26" aria-hidden="true"><rect x="2" y="7" width="17" height="17" fill="none" stroke="var(--grey)" stroke-width="2"/><path d="M6 14l5 5L23 4" fill="none" stroke="var(--orange)" stroke-width="3.5"/></svg>Pull down tall masts</li>
  </ul>

  <div class="phone">
    <svg viewBox="0 0 50 50" aria-hidden="true"><circle cx="25" cy="25" r="22" fill="none" stroke="var(--white)" stroke-width="3"/><path d="M18 13c2-1 4 4 3 6l-2 2c1 4 4 7 8 9l2-2c2-1 7 1 6 3l-1 3c-1 2-4 3-7 1-6-3-11-9-13-15-1-3 1-6 4-7Z" fill="var(--white)"/></svg>
    <span>0452 736 205</span>
  </div>
</div>
</body>
</html>
```